Web Design Project for starting CCTV/Camera security installer/reseller

Hello,

An old class mate is starting his own little CCTV/Camera security business as a one-man-gang.

He asked me to do his website but unfortunatly my design skills are not worth looking at :) The coding is no problem.

So I'm here to request a design.

What he wants is a site that lists the products he might install which is based on a small tree structure. So see it as a shop overview/display but without the baskets & cashout options.

you can find a site structure scheme, logo, product images & data sheet pdf's at this filvaultra address:

https://www.filvaultra.com/sh/kq7zt3908wx4pl2/vnRtLoBe5y/Lumo-Ward

the site itself is http://www.lumo-ward.be but only has a splash screen until I have a design for it.

the logo is a bit out of proportions, not sure if you can make something good out of it :/

Most content is in Dutch, I'll see if I can translate the needed parts...
Updates

Dear designers,

I have some good new for you.

You are allowed to use only that chrome Lumo-Ward part of the logo,
which should make things a lot easier to fit into your design ideas.

Keep up the creativity!

Dear designers,

I uploaded a new logo to the filvaultra space.

It's a png but unfortunately it's not transparent, I'm still waiting for that one
but you know how to erase it in photoshop.

Target Market(s)

people looking for a visual solution to protect their company/home

Industry/Entity Type

Security

Requirements
Must have
• an iconized way to browse/display a tree. (not the traditional folder/explorer style)

maybe first a page with buttons/icons showing level 1 the group types (IP cams, IP servers, Accessories)

level 2 product groups (dome cam, ptz cam etc)

level 3 the actual product + a link to a pdf datasheet (if any)

could be multipage or maybe in/on-page since the product list won't be that huge.

maybe some random product info left and/or right so that the content area is not massive since he has not much to type
;)

```html
<!DOCTYPE html>
<html lang="en">
<head>
<meta charset="utf-8">
<title>Lumo-Ward Camera surveillance</title>
<link href="https://fonts.googleapis.com/css2?family=PT+Sans:wght@400;700&display=swap" rel="stylesheet">
<style>
:root{
  --blue-top:#6aa6ec;
  --blue-bottom:#2f72c9;
  --blue-edge:#2a63b0;
  --heading:#2a4f86;
  --text:#555;
  --text-soft:#777;
  --panel:#f3f2f3;
  --strip-top:#c9c9c9;
  --strip-bottom:#9e9e9e;
  --white:#fff;
}
*{margin:0;padding:0;box-sizing:border-box}
html,body{width:1200px;height:1031px;overflow:hidden}
body{position:relative;background:var(--white);font-family:"PT Sans",sans-serif;color:var(--text)}
.abs{position:absolute}
.top-band{left:0;top:0;width:1200px;height:516px;background:linear-gradient(#fff 0%,#f2f2f2 40%,#e2e2e2 100%)}
.brand{display:flex;align-items:center;gap:8px;font-size:24px;color:var(--heading);letter-spacing:1px}
.brand .mark{width:14px;height:14px;background:var(--blue-bottom);border-radius:50%}
.brand-top{left:0;width:1200px;top:62px;justify-content:center}
.nav{left:150px;top:128px;width:900px;height:43px;border-radius:5px 5px 0 0;background:linear-gradient(var(--blue-top),var(--blue-bottom));border:1px solid var(--blue-edge);box-shadow:inset 0 1px 0 rgba(255,255,255,.5)}
.nav a{position:absolute;top:12px;color:var(--white);font-size:12px;text-decoration:none}
.hero{left:150px;top:171px;width:900px;height:248px;background:linear-gradient(90deg,#f1f1f2,#f7f7f8 60%,#ececee)}
.hero h1{position:absolute;left:22px;top:50px;font-size:17px;font-weight:400;color:var(--heading)}
.hero h1 b{font-weight:700}
.hero p{position:absolute;left:23px;top:84px;font-size:11.5px;line-height:22.5px;color:var(--text)}
.btn{display:flex;align-items:center;justify-content:center;background:linear-gradient(var(--blue-top),var(--blue-bottom));color:var(--white);font-size:12px;border-radius:2px;border:1px solid var(--blue-edge)}
.hero .btn{position:absolute;left:22px;top:139px;width:103px;height:28px}
.hero-photo{left:548px;top:0;width:300px;height:238px;background:linear-gradient(160deg,#ececee,#d9dadd)}
.strip{left:150px;top:419px;width:900px;height:65px;border-radius:0 0 8px 8px;background:linear-gradient(var(--strip-top),var(--strip-bottom))}
.strip .notch{position:absolute;left:248px;top:-8px;width:0;height:0;border-left:8px solid transparent;border-right:8px solid transparent;border-bottom:8px solid var(--strip-top)}
.thumb{position:absolute;top:12px;width:58px;height:37px;border:1px solid #fff;background:linear-gradient(#e8e8e8,#8a8a8a)}
.strip-text{position:absolute;top:9px;font-size:13px;line-height:21px;color:#eee}
.strip-text b{color:var(--white)}
.panel{background:var(--panel);border-radius:6px 6px 4px 4px}
.panel-head{height:39px;border-radius:5px 5px 0 0;background:linear-gradient(var(--blue-top),var(--blue-bottom));border-bottom:2px solid var(--blue-edge);color:#eaf2fc;font-size:14px;padding:9px 20px}
.services{left:150px;top:534px;width:216px;height:313px}
.services ul{list-style:none;position:absolute;left:20px;top:46px}
.services li{font-size:11px;color:var(--text);height:22.5px;display:flex;align-items:center;gap:9px}
.services li.main{color:#333}
.services li.main::before{content:"";border-left:5px solid var(--blue-bottom);border-top:4px solid transparent;border-bottom:4px solid transparent;margin-right:5px}
.services li.sub::before{content:"";width:4px;height:4px;border-radius:50%;background:#9bb8dc;margin-right:1px}
.services li.gap{margin-top:3px}
.products{left:378px;top:534px;width:672px;height:313px}
.card{position:absolute;top:56px;width:202px}
.card .photo{height:111px;background:linear-gradient(#fff,#f3f3f4)}
.card h3{margin-top:14px;font-size:13px;font-weight:400;color:#222}
.card p{margin-top:7px;font-size:10.5px;line-height:17px;color:var(--text-soft)}
.card .more{margin-top:7px;font-size:11px;color:#333;display:block}
.foot-title{font-size:14px;color:var(--heading);font-weight:400}
.contact-lines{left:169px;top:892px;font-size:11px;line-height:22.5px;color:var(--text)}
.email{left:378px;top:896px;width:216px;height:26px;border:1px solid #bbb;border-radius:6px;background:linear-gradient(#e6e6e6,#fff);font-size:12px;color:#888;padding:4px 14px}
.subscribe{left:491px;top:944px;width:103px;height:28px}
.social{top:895px;width:22px;height:22px;border-radius:3px;background:linear-gradient(var(--blue-top),var(--blue-bottom))}
.brand-foot{left:943px;top:897px;font-size:14px}
.brand-foot .mark{width:9px;height:9px}
.bottom-bar{left:0;top:991px;width:1200px;height:40px;background:#dcdcdc;font-size:11.5px;color:#555}
.bottom-bar .copy{position:absolute;left:151px;top:13px}
.bottom-bar .legal{position:absolute;right:150px;top:12px}
.bottom-bar .legal span{margin:0 9px}
</style>
</head>
<body>
<div class="abs top-band"></div>
<div class="abs brand brand-top"><span class="mark"></span>Lumo-Ward</div>

<nav class="abs nav">
  <a style="left:66px">Home</a>
  <a style="left:144px">Company</a>
  <a style="left:240px">Products</a>
  <a style="left:332px">Solutions</a>
  <a style="left:489px">Support</a>
  <a style="left:577px">Online Store</a>
  <a style="left:688px">Contact Us</a>
  <a style="left:792px">Sitemap</a>
</nav>

<section class="abs hero">
  <h1>Welcome at <b>Lumo-Ward Camera surveillance</b></h1>
  <p>We offer a large amount of surveillance camera's<br>video storage systems and surveillance monitors.</p>
  <a class="btn">Read More..</a>
  <div class="abs hero-photo" role="img" aria-label="Photo of a white dome surveillance camera"></div>
</section>

<div class="abs strip">
  <div class="notch"></div>
  <div class="thumb" style="left:17px" role="img" aria-label="Dome camera thumbnail"></div>
  <div class="strip-text" style="left:94px">Camera system for<br><b>Home</b></div>
  <div class="thumb" style="left:228px" role="img" aria-label="Bullet camera thumbnail"></div>
  <div class="strip-text" style="left:305px">Camera system for<br><b>Office</b></div>
  <div class="thumb" style="left:456px" role="img" aria-label="Dome camera thumbnail"></div>
  <div class="strip-text" style="left:533px">Camera <b>surveillance</b></div>
  <div class="thumb" style="left:683px" role="img" aria-label="Bullet camera thumbnail"></div>
  <div class="strip-text" style="left:760px">Camera system for<br><b>Office</b></div>
</div>

<section class="abs panel services">
  <div class="panel-head">Our Services</div>
  <ul>
    <li class="main">A V Door Entry Systems</li>
    <li class="main">Access Control Systems</li>
    <li class="main">CCTV Surveillance</li>
    <li class="sub gap">Camera Housing &amp; Accessories</li>
    <li class="sub">Digital Recorder</li>
    <li class="sub">IP CameraMonitor &amp; Display</li>
    <li class="sub">Network Video Server</li>
    <li class="sub">Power Supply &amp; UPS</li>
    <li class="sub">Storage Media</li>
    <li class="sub">Surveillance Software</li>
  </ul>
</section>

<section class="abs panel products">
  <div class="panel-head">Our Products</div>
  <article class="card" style="left:14px">
    <div class="photo" role="img" aria-label="White dome camera product photo"></div>
    <h3>LWD - K310P/K310N</h3>
    <p>Lorem Ipsum is simply dummy text of<br>the printing and typesetting industry.<br>Lorem Ipsum has been the industry's<br>standard dummy text eve</p>
    <a class="more">Read More..</a>
  </article>
  <article class="card" style="left:238px">
    <div class="photo" role="img" aria-label="Black dome camera product photo"></div>
    <h3>LWD - K310P/K310N</h3>
    <p>Lorem Ipsum is simply dummy text of<br>the printing and typesetting industry.<br>Lorem Ipsum has been the industry's<br>standard dummy text eve</p>
    <a class="more">Read More..</a>
  </article>
  <article class="card" style="left:456px">
    <div class="photo" role="img" aria-label="Bullet camera product photo"></div>
    <h3>LWD - K310P/K310N</h3>
    <p>Lorem Ipsum is simply dummy text of<br>the printing and typesetting industry.<br>Lorem Ipsum has been the industry's<br>standard dummy text eve</p>
    <a class="more">Read More..</a>
  </article>
</section>

<h4 class="abs foot-title" style="left:167px;top:867px">Contact Information</h4>
<div class="abs contact-lines">Phone : 000 000 0000<br>Cell &nbsp;&nbsp;&nbsp;: 000 000 0000<br>Fax &nbsp;&nbsp;&nbsp;: 000 000 0000</div>

<h4 class="abs foot-title" style="left:378px;top:867px">Sign up for Newsletter</h4>
<div class="abs email">Email Id</div>
<a class="abs btn subscribe">Subscribe</a>

<h4 class="abs foot-title" style="left:634px;top:867px">Follow Us On :</h4>
<div class="abs social" style="left:634px" role="img" aria-label="Social network link"></div>
<div class="abs social" style="left:667px" role="img" aria-label="Social network link"></div>
<div class="abs social" style="left:701px" role="img" aria-label="Social network link"></div>

<div class="abs brand brand-foot"><span class="mark"></span>Lumo-Ward</div>

<footer class="abs bottom-bar">
  <div class="copy">Copyright © 2012. All Rights Reserved</div>
  <div class="legal">Terms &amp; Condition<span>|</span>Privacy Policy</div>
</footer>
</body>
</html>
```